Large multi-office optometry business opening a Dry Eye Spa and needs sign.

Business name/sign info: Brenwick Dry Eye Institute, (555) 362-4817
Backlit pole sign at office entrance on a very busy street
Sign dimensions: 53" tall x 136.5" wide
State of the art Dry Eye Spa for treatment of all forms of dry eye and ocular surface disease. Also, have aesthetics treatments (IPL, Low Level Light Treatment, etc.)

Target Market(s)

People who are suffering from: dryness, burning, foreign body sensation, itching, fluctuating vision, tired eyes, etc.

Industry/Entity Type

Optometry and aesthetics

Colors
0054AA
0677BA
7BADD7
CADEEF
E8F1F8

Requirements
Must have
• Business name, phone number, subliminal message of relief in a glance or short look.
Nice to have
• Cool, relief, soothing sense.
Should not have
• Too much information or too busy.

```html
<!DOCTYPE html>
<html lang="en">
<head>
<meta charset="utf-8">
<title>Brenwick Dry Eye Institute – Pole Sign</title>
<link href="https://fonts.googleapis.com/css2?family=Anton&family=Bebas+Neue&family=Yellowtail&display=swap" rel="stylesheet">
<style>
  :root {
    --page-bg: #d9dee4;
    --sign-bg: #111112;
    --sign-bg-edge: #0b0b0c;
    --text-light: #f1f1f2;
    --text-shade: #c9c9cc;
    --accent: #4cc0ea;
    --accent-script: #5cc6e6;
    --divider: #3aa6c4;
  }
  * { margin: 0; padding: 0; box-sizing: border-box; }
  html, body {
    width: 1200px; height: 717px; overflow: hidden;
    background: var(--page-bg);
  }
  .sign {
    position: absolute; left: 0; top: 129px;
    width: 1200px; height: 459px;
    background: radial-gradient(ellipse at 45% 45%, var(--sign-bg) 0%, var(--sign-bg-edge) 100%);
    color: var(--text-light);
  }
  .brand-name {
    position: absolute; left: 0; width: 785px; top: 44px;
    text-align: center;
    font-family: "Anton", sans-serif;
    font-size: 158px; line-height: 1; letter-spacing: 4px;
    background: linear-gradient(180deg, var(--text-light) 30%, var(--text-shade) 100%);
    -webkit-background-clip: text; background-clip: text; color: transparent;
  }
  .brand-sub {
    position: absolute; left: 0; width: 785px; top: 210px;
    text-align: center;
    font-family: "Bebas Neue", sans-serif;
    font-size: 80px; line-height: 1; letter-spacing: 1px;
    color: var(--accent);
  }
  .dot-rule {
    position: absolute; left: 104px; top: 306px;
    width: 580px; height: 6px;
    background-image: radial-gradient(circle, var(--accent) 2.6px, transparent 3px);
    background-size: 26.4px 6px;
    background-repeat: repeat-x;
  }
  .contact {
    position: absolute; left: 0; width: 785px; top: 343px;
    text-align: center;
    font-family: "Bebas Neue", sans-serif;
    font-size: 76px; line-height: 1; letter-spacing: 0.5px;
    color: var(--text-light);
  }
  .divider {
    position: absolute; left: 758px; top: 58px;
    width: 2px; height: 346px;
    background: linear-gradient(180deg, transparent, var(--divider) 12%, var(--divider) 88%, transparent);
  }
  .tagline {
    position: absolute; left: 838px; top: 44px;
    font-family: "Yellowtail", cursive;
    font-size: 42px; line-height: 44px;
    color: var(--accent-script);
  }
  .services { position: absolute; left: 840px; top: 157px; list-style: none; }
  .service {
    display: flex; align-items: center;
    height: 72px; margin-bottom: 17px;
  }
  .service-photo {
    width: 72px; height: 72px; border-radius: 50%;
    flex: none; margin-right: 14px;
  }
  .photo-exam { background: radial-gradient(circle at 45% 40%, #e9b58a, #c27c4b 55%, #7f96b4); }
  .photo-anatomy { background: radial-gradient(circle at 55% 50%, #f08a3a, #c9413a 55%, #e9d9d6); }
  .photo-eye { background: radial-gradient(circle at 50% 50%, #5d8f96, #b28a70 45%, #7a5440); }
  .service-label {
    font-family: "Bebas Neue", sans-serif;
    font-size: 33px; line-height: 28px;
    color: var(--text-light);
  }
</style>
</head>
<body>
  <main class="sign">
    <h1 class="brand-name">BRENWICK</h1>
    <h2 class="brand-sub">DRY EYE INSTITUTE</h2>
    <div class="dot-rule"></div>
    <p class="contact">CONTACT : (555) 362-4817</p>

    <div class="divider"></div>

    <p class="tagline">State of the art<br>Dry Eye Spa</p>
    <ul class="services">
      <li class="service">
        <div class="service-photo photo-exam" role="img" aria-label="Photo of a patient during an eye examination"></div>
        <span class="service-label">ALL FORMS<br>OF DRY EYE</span>
      </li>
      <li class="service">
        <div class="service-photo photo-anatomy" role="img" aria-label="Illustration of eye anatomy cross-section"></div>
        <span class="service-label">OCULAR SURFACE<br>DISEASE</span>
      </li>
      <li class="service">
        <div class="service-photo photo-eye" role="img" aria-label="Close-up photo of an eye"></div>
        <span class="service-label">AESTHETICS<br>TREATMENT</span>
      </li>
    </ul>
  </main>
</body>
</html>
```